Bright Path Mentors Needs A New Website Design

We need a 8 page website designed for "Bright Path Mentors .ca" similar in design to: "quill ridge learning .com".

The winner/successful candidate on the home page will be asked to complete the following inner pages to complete the project:

About Us
Philosophy
How We Work
Work With Us
Blog
Find A Tutor
Contact

Target Market(s)

Tutoring business clients/children

Industry/Entity Type

Education

Number of Pages Required

5+ page

Font styles to use
Sans Serif

Requirements
Must have
• The attached logo included of course. Similar design to the design provided above in the brief. Clear high quality high resolution images of children in school settings.

```html
<!DOCTYPE html>
<html lang="en">
<head>
<meta charset="utf-8">
<title>Bright Path Mentors</title>
<link href="https://fonts.googleapis.com/css2?family=Raleway:wght@400;500;600;700&family=Open+Sans:wght@400;600&display=swap" rel="stylesheet">
<style>
:root{
  --blue:#2b3592;
  --blue-dark:#232c7e;
  --orange:#f7941d;
  --orange-deep:#e07c0c;
  --ink:#333;
  --muted:#777;
  --paper:#f5f4f6;
  --footer:#222;
  --footer-base:#111;
  --services:#3d4550;
  --chalk:#1e2a22;
}
*{box-sizing:border-box;margin:0;padding:0}
html,body{width:1200px;height:2332px;overflow:hidden}
body{font-family:'Raleway',sans-serif;color:var(--ink);background:#fff;position:relative}
section,header,footer,article{position:absolute;left:0;width:1200px}
a{color:inherit;text-decoration:none}
.body-text{font-family:'Open Sans',sans-serif}

/* hero */
.hero{top:0;height:455px;overflow:hidden}
.hero-photo{position:absolute;inset:0;background:linear-gradient(100deg,#6e3a2c 0%,#9a6a52 25%,#c9b7a8 45%,#8f6a58 60%,#d8d2cc 80%,#b7aea6 100%)}
.topbar{position:absolute;top:6px;right:249px;display:flex;align-items:center;gap:8px;font-size:12px;color:#333}
.social-dot{width:9px;height:9px;border-radius:50%;background:#333}
.topbar .phone{margin-left:16px;display:flex;align-items:center;gap:5px}
.brand{position:absolute;left:255px;top:8px;display:flex;align-items:center;gap:6px}
.brand-mark{width:14px;height:14px;border-radius:50%;background:var(--blue)}
.brand-name{font-size:13px;font-weight:700;color:var(--blue)}
.main-nav{position:absolute;top:38px;left:549px;display:flex;gap:13px;font-size:10.5px;color:#333}
.main-nav a.active{border-bottom:2px solid var(--blue);padding-bottom:3px;color:var(--blue)}
.welcome{position:absolute;left:252px;top:121px;width:282px;height:282px;border-radius:50%;background:rgba(20,20,20,.78);text-align:center;color:#fff;padding:62px 40px 0}
.welcome h1{font-size:13.5px;font-weight:600;white-space:nowrap;padding-bottom:8px;border-bottom:2px solid #fff;margin:0 -14px 10px}
.welcome h1 span{color:var(--orange)}
.welcome p{font-size:9px;line-height:1.4}
.btn{display:inline-block;background:linear-gradient(#fba93c,var(--orange-deep));color:#fff;border-radius:3px;font-family:'Raleway',sans-serif}
.welcome .btn{margin-top:16px;width:130px;line-height:30px;font-size:14px}

/* features */
.features{top:455px;height:132px;background:var(--blue);display:flex;padding-left:249px}
.feature{width:233px;padding:12px 14px 0 8px;border-right:1px solid rgba(255,255,255,.15);color:#fff}
.feature:last-child{border-right:0}
.feature h3{color:var(--orange);font-size:14px;font-weight:500;margin:8px 0 6px}
.feature p{font-size:8.5px;line-height:1.35}

/* private tutoring */
.private{top:587px;height:280px;background:var(--paper)}
.private h2{position:absolute;left:249px;top:22px;font-size:26px;font-weight:500;color:var(--blue)}
.private p{position:absolute;left:249px;top:74px;width:390px;font-size:9.5px;line-height:1.65;color:var(--muted)}
.private-photo{position:absolute;left:660px;top:24px;width:291px;height:244px;background:linear-gradient(135deg,#d8dde3,#b9a592 50%,#eceff2)}

/* services */
.services{top:867px;height:244px;background:linear-gradient(#2f3640,var(--services) 50%,#4c5560);text-align:center;color:#fff}
.services h2{position:absolute;top:28px;width:100%;font-size:26px;font-weight:500;color:var(--orange)}
.service{position:absolute;top:86px;width:180px;margin-left:-90px}
.service-icon{width:52px;height:52px;border-radius:50%;border:2px solid var(--orange);background:var(--blue);margin:0 auto 10px;display:flex;align-items:center;justify-content:center}
.service h3{font-size:12px;font-weight:500;color:var(--orange);margin-bottom:3px}
.service p{font-size:8.5px;line-height:1.3}

/* promo */
.promo{top:1111px;height:253px;background:radial-gradient(ellipse at center,#2a3a2f,var(--chalk) 70%);text-align:center;color:#fff}
.promo h2{margin-top:58px;font-size:26px;font-weight:500;color:var(--orange)}
.promo p{width:580px;margin:18px auto 0;font-size:9px;line-height:1.4}
.promo .btn{margin-top:34px;width:171px;line-height:36px;font-size:16px;border:1px solid #fff3}

/* testimonials */
.video{top:1392px;left:249px;width:376px;height:237px;border:1px solid var(--blue);background:linear-gradient(135deg,#dfe6d2,#b68a6e 45%,#d46c8f 65%,#e5e9e0)}
.play{position:absolute;left:50%;top:50%;width:52px;height:52px;margin:-26px 0 0 -26px;border-radius:50%;border:2px solid #fff;background:rgba(255,255,255,.35)}
.play::after{content:"";position:absolute;left:20px;top:14px;border-left:16px solid #fff;border-top:11px solid transparent;border-bottom:11px solid transparent}
.testimonials{top:1392px;left:631px;width:319px;height:237px;background:var(--paper);text-align:center}
.testimonials h2{margin-top:16px;font-size:26px;font-weight:500;color:var(--blue)}
.testimonials .name{margin-top:6px;font-size:10px;color:var(--orange)}
.testimonials .place{font-size:8px;color:var(--muted)}
.testimonials .quote{width:200px;margin:8px auto 0;font-size:8.5px;line-height:1.35;color:var(--muted)}
.t-brand{position:absolute;left:40px;top:150px;display:flex;flex-direction:column;align-items:center;gap:4px}
.t-brand .brand-mark{width:34px;height:34px}
.t-brand .brand-name{font-size:10px}
.seal{position:absolute;right:42px;top:150px;width:68px;height:68px;border-radius:50%;background:radial-gradient(#f3d15a,#c7951c)}

/* blog */
.blog-title{top:1652px;text-align:center;font-size:26px;font-weight:500;color:var(--blue)}
.blog-card{top:1694px;width:224px;height:334px;border:1px solid #ddd;background:#fff;overflow:hidden}
.blog-photo{height:144px}
.blog-card h3{margin:14px 10px 6px;font-size:14px;font-weight:500;color:var(--blue)}
.blog-card p{margin:0 10px;font-size:8.5px;line-height:1.5;color:#555}
.blog-foot{position:absolute;left:0;bottom:0;width:100%;height:22px;border-top:1px solid #ddd;background:#fff;display:flex;justify-content:space-between;align-items:center;font-size:8px;color:#777;padding-right:8px}
.blog-foot .btn{border-radius:0;width:96px;line-height:22px;text-align:center;font-size:9px}

/* newsletter */
.newsletter{top:2045px;height:39px;background:var(--blue);display:flex;align-items:center;justify-content:center;gap:14px;color:#fff}
.newsletter h2{font-size:17px;font-weight:500}
.newsletter .field{width:232px;height:18px;background:#fff;color:#999;font-size:9px;font-style:italic;padding:3px 8px}
.newsletter .btn{border-radius:0;width:114px;line-height:22px;text-align:center;font-size:12px}

/* footer */
.site-footer{top:2084px;height:222px;background:var(--footer);color:#ccc}
.footer-col{position:absolute;top:26px;font-size:9.5px;line-height:17.5px}
.footer-col h4{font-size:12.5px;font-weight:500;color:var(--orange);margin-bottom:8px}
.footer-col li{list-style:none}
.footer-col li::before{content:"› ";color:#fff}
.footer-col li.current{color:var(--orange)}
.contact-list li::before{content:"";display:inline-block;width:6px;height:6px;border-radius:50%;background:var(--orange);margin-right:6px}
.social-list{text-align:center}
.social-list span{display:block;width:9px;height:9px;border-radius:50%;background:#777;margin:8px auto 9px}
.copyright{top:2306px;height:26px;background:var(--footer-base);color:#fff;font-size:8px;text-align:center;line-height:26px}
</style>
</head>
<body>

<header class="hero">
  <div class="hero-photo" role="img" aria-label="Smiling student with a backpack in a school hallway"></div>
  <div class="topbar">
    <span class="social-dot"></span><span class="social-dot"></span><span class="social-dot"></span><span class="social-dot"></span>
    <span class="phone">
      <svg width="10" height="10" viewBox="0 0 24 24"><path fill="#333" d="M6.6 10.8a15 15 0 0 0 6.6 6.6l2.2-2.2a1 1 0 0 1 1-.3 11 11 0 0 0 3.6.6 1 1 0 0 1 1 1V20a1 1 0 0 1-1 1A17 17 0 0 1 3 4a1 1 0 0 1 1-1h3.5a1 1 0 0 1 1 1c0 1.2.2 2.4.6 3.6a1 1 0 0 1-.3 1z"/></svg>
      1-855-310-7724
    </span>
  </div>
  <a class="brand" href="#"><span class="brand-mark"></span><span class="brand-name">Bright Path Mentors</span></a>
  <nav class="main-nav">
    <a class="active" href="#">Home</a><a href="#">About Us</a><a href="#">Philosophy</a><a href="#">How We Work</a><a href="#">Work With Us</a><a href="#">Blog</a><a href="#">Find A Tutor</a><a href="#">Contact</a>
  </nav>
  <div class="welcome">
    <h1>Welcome to <span>Bright Path Mentors</span></h1>
    <p class="body-text">Lorem Ipsum is simply dummy text of the printing and typesetting industry. Lorem Ipsum has been the industry's standard dummy text ever since the 1500s, when an unknown printer took a galley of type and scrambled it to make a type specimen book. It has survived not only five</p>
    <a class="btn" href="#">Join Us!</a>
  </div>
</header>

<section class="features">
  <div class="feature">
    <svg width="20" height="20" viewBox="0 0 20 20" fill="none" stroke="#fff" stroke-width="1.5"><rect x="2" y="2" width="16" height="11"/><path d="M6 18h8M10 13v5"/></svg>
    <h3>How We Operate</h3>
    <p class="body-text">Lorem Ipsum is simply dummy text of the printing andtypesetting industry. Lorem Ipsum has been the industry's standard dummy text ever since the 1500s, when an unknown printer took a galley of type and</p>
  </div>
  <div class="feature">
    <svg width="20" height="20" viewBox="0 0 20 20" fill="none" stroke="#fff" stroke-width="1.5"><rect x="2" y="2" width="16" height="12"/><circle cx="10" cy="7" r="2.5"/><path d="M5 18h10"/></svg>
    <h3>Tutor Selection Process</h3>
    <p class="body-text">Lorem Ipsum is simply dummy text of the andtypesetting industry. Lorem Ipsum has industry's standard dummy text ever since the 1500s, when an unknown printer took a galley of type and</p>
  </div>
  <div class="feature">
    <svg width="20" height="20" viewBox="0 0 20 20" fill="none" stroke="#fff" stroke-width="1.5"><rect x="2" y="3" width="16" height="11"/><path d="M7 8l2 2 4-4M6 18h8"/></svg>
    <h3>Online Tutoring</h3>
    <p class="body-text">Lorem Ipsum is simply dummy text of the printing andtypesetting industry. Lorem Ipsum has been the industry's standard dummy text ever since the 1500s, when an unknown printer took a galley of type and</p>
  </div>
</section>

<section class="private">
  <h2>Private Home Tutoring</h2>
  <p class="body-text">Lorem Ipsum is simply dummy text of the printing and typesetting industry. Lorem Ipsum has been the industry's standard dummy text ever since the 1500s, when an unknown printer took a galley of type and scrambled it to make a type specimen book. It has survived not only five centuries, but also the leap into electronic typesetting, remaining essentially unchanged. It was popularised in the 1960s with the release of Letraset sheets containing Lorem Ipsum passages, and more recently with desktop publishing software like Aldus PageMaker including versions of Lorem Ipsum.</p>
  <div class="private-photo" role="img" aria-label="Student writing at a desk in a classroom"></div>
</section>

<section class="services" role="group" aria-label="Our Services">
  <h2>Our Services</h2>
  <div class="service" style="left:314px">
    <div class="service-icon"><svg width="22" height="22" viewBox="0 0 22 22" fill="none" stroke="#fff" stroke-width="1.6"><rect x="3" y="3" width="16" height="11"/><path d="M7 19l4-5 4 5"/></svg></div>
    <h3>Home Tutors</h3>
    <p class="body-text">Lorem Ipsum is simply dummy text of the printing and typesetting industry. Lorem Ipsum has been1500s, when</p>
  </div>
  <div class="service" style="left:503px">
    <div class="service-icon"><svg width="22" height="22" viewBox="0 0 22 22"><rect x="3" y="6" width="11" height="10" rx="1" fill="#fff"/><path d="M14 10l5-3v8l-5-3z" fill="#fff"/></svg></div>
    <h3>Video Tutorial</h3>
    <p class="body-text">Lorem Ipsum is simply dummy text of the printing and typesetting industry. Lorem Ipsum has been1500s, when</p>
  </div>
  <div class="service" style="left:699px">
    <div class="service-icon"><svg width="22" height="22" viewBox="0 0 22 22" fill="none" stroke="#fff" stroke-width="1.6"><rect x="3" y="4" width="16" height="11"/><path d="M8 19h6M11 15v4"/></svg></div>
    <h3>Online Education</h3>
    <p class="body-text">Lorem Ipsum is simply dummy text of the printing and typesetting industry. Lorem Ipsum has been1500s, when</p>
  </div>
  <div class="service" style="left:886px">
    <div class="service-icon"><svg width="22" height="22" viewBox="0 0 22 22" fill="none" stroke="#fff" stroke-width="1.6"><path d="M4 17L17 4M7 17h-3v-3M15 8l3 3"/></svg></div>
    <h3>All Education</h3>
    <p class="body-text">Lorem Ipsum is simply dummy text of the printing and typesetting industry. Lorem Ipsum has been1500s, when</p>
  </div>
</section>

<section class="promo">
  <h2>FIRST SESSION JUST $7! All SUBJECTS! ALL GRADES!</h2>
  <p class="body-text">Lorem Ipsum is simply dummy text of the printing and typesetting industry. Lorem Ipsum has been the industry's standard dummy text ever since the 1500s, when an unknown printer took a galley of type and scrambled it to make a type specimen book. It has survived not only five centuries, but also the leap into electronic typesetting.</p>
  <a class="btn" href="#">BOOK NOW</a>
</section>

<section class="video" role="img" aria-label="Video of a student holding books and a phone outdoors"><span class="play"></span></section>
<section class="testimonials">
  <h2>Our Testimonials</h2>
  <div class="name">Nora L.</div>
  <div class="place">Vaughan, Ontario</div>
  <p class="quote body-text">Clara Mendes Dear Ms. Mendes, RE: Highest Recommendation for Tutoring Services. I take this opportunity to give the highest...</p>
  <div class="t-brand"><span class="brand-mark"></span><span class="brand-name">Bright Path Mentors</span></div>
  <div class="seal" role="img" aria-label="Guarantee seal"></div>
</section>

<section class="blog-title">Our Blog</section>
<article class="blog-card" style="left:249px">
  <div class="blog-photo" role="img" aria-label="Student peeking over a stack of books" style="background:linear-gradient(135deg,#5a4a3e,#c9a27a 50%,#e6e2dc)"></div>
  <h3>Online Education</h3>
  <p class="body-text">Lorem Ipsum is simply dummy text of the printing and typesetting industry. Lorem Ipsum has been the industry's standard dummy text ever since the 1500s, when an unknown printer took a galley of type and scrambled it to make a type specimen book. It has survived not only five centuries, but also the leap into electronic typesetting, remaining essentially unchanged. It was popularised in the 1960s with the</p>
  <div class="blog-foot"><a class="btn" href="#">READ MORE</a><span>comment</span></div>
</article>
<article class="blog-card" style="left:488px">
  <div class="blog-photo" role="img" aria-label="Teacher holding folders in a school" style="background:linear-gradient(135deg,#cfd3d6,#8a6a58 50%,#e8e6e2)"></div>
  <h3>Online Education</h3>
  <p class="body-text">Lorem Ipsum is simply dummy text of the printing and typesetting industry. Lorem Ipsum has been the industry's standard dummy text ever since the 1500s, when an unknown printer took a galley of type and scrambled it to make a type specimen book. It has survived not only five centuries, but also the leap into electronic typesetting, remaining essentially unchanged. It was popularised in the 1960s with the</p>
  <div class="blog-foot"><a class="btn" href="#">READ MORE</a><span>comment</span></div>
</article>
<article class="blog-card" style="left:726px">
  <div class="blog-photo" role="img" aria-label="Two young girls smiling at school" style="background:linear-gradient(135deg,#f0d9a8,#e0a87c 50%,#8fb7d8)"></div>
  <h3>Online Education</h3>
  <p class="body-text">Lorem Ipsum is simply dummy text of the printing and typesetting industry. Lorem Ipsum has been the industry's standard dummy text ever since the 1500s, when an unknown printer took a galley of type and scrambled it to make a type specimen book. It has survived not only five centuries, but also the leap into electronic typesetting, remaining essentially unchanged. It was popularised in the 1960s with the</p>
  <div class="blog-foot"><a class="btn" href="#">READ MORE</a><span>comment</span></div>
</article>

<section class="newsletter">
  <h2>Subscribe to Olur Newsletter</h2>
  <div class="field">Enter Email</div>
  <a class="btn" href="#">Subscribe</a>
</section>

<footer class="site-footer">
  <div class="footer-col" style="left:249px"><h4>Site Map</h4><ul>
    <li class="current">Home</li><li>About Us</li><li>Philosophy</li><li>How We Work</li><li>Work With Us</li><li>Blog</li><li>Find A Tutor</li><li>Contact</li></ul></div>
  <div class="footer-col" style="left:373px"><h4>Subjects</h4><ul>
    <li>Elementary Tutoring</li><li>Foreign Languages</li><li>Math Tutoring</li><li>Science Tutoring</li></ul></div>
  <div class="footer-col" style="left:519px"><h4>Other Subjects</h4><ul>
    <li>Elementary Math Tutoring</li><li>Elementary Tutoring</li><li>Foreign Languages</li><li>Elementary Math Tutoring</li><li>Elementary School Math</li><li>Online Tutoring</li><li>Phonics Tutoring</li><li>Reading Tutoring</li><li>Biology Tutoring</li></ul></div>
  <div class="footer-col contact-list" style="left:696px"><h4>Contact</h4><ul>
    <li>1280 Maple Crest Road, Suite 210</li><li>Toronto</li><li>Ontario</li><li>M4B 2K7</li><li>1-855-310-7724</li><li>info@brightpathmentors.ca</li></ul></div>
  <div class="footer-col social-list" style="left:883px"><h4>Social Media</h4>
    <span></span><span></span><span></span><span></span></div>
</footer>
<section class="copyright">© 2016 All Rights Bright Path Mentors</section>

</body>
</html>
```